New Vidora Channel Banner Graphic/Logo for "Cozy Nook Attic Sound"

Create a banner for my new Vidora channel for Cozy Nook Attic Sound. This is partially a logo project, but the logo will not be used elsewhere. Check out Vidora channels to see the banners others have created. This channel is about my home studio, the gear, microphones, musical instruments, wiring, software etc. that goes into a home studio. It's a free channel, made for sharing information. This is a graphic design that will be posted on vidora using built-in vidora tools.
Updates

More information about this project! I'm staring a channel called "Cozy Nook Attic Sound" on vidorastream.net. I need a deign for this banner and a logo for Cozy Nook Attic Sound. I called the channel by that name because my music studio is my happy place. It's about music and instruments (gutars, piano, drums, percussion) singing (microhpones), creativity, and what you'd expect form musicians. It's also about technology, recording, live-streaming, music videos, etc. It is my hobby, not my profession. I will be creating content for other amateur home studio aficionados and hobbyists. There are a lot of home studio channels and videos you can look at on vidora to get a flavor for musicians and studios. Usually fairly tech-heavy. An appeal of my channel will be a very approachable, "i'm the same as you" welcome for people that are doing it to enjoy it.

I put this project in the wrong category to start. This has been fixed, but I think benefits I would have received (such as invited designers) and announcement of project in the correct category mean I'm not getting designers. Your initial menu should be improved. I'm having a banner created for a web page in Vidora. I think it is easy to mistake that for a web design when it is really a graphic design for the web.

Target Market(s)

Similar to myself, people as interested in studio/production tech as they are in making music, perhaps trending a bit older and successful enough to afford some gear!

Number of Pages Required

1 page

Font styles to use
Sans Serif

Requirements
Must have
• This is not really a web design, i may have miscategorized. Please see uploaded docs for pics of similar banner on a Vidora page. ADDED 1/5: As this is a vidora channel that could be viewed on any device, the banner should be friendly in this way and design or design variations needed for PC, Tabrix, phone vie3wing.

Here are the Vidora size specs:
Banner image guidelines
Your banner image must meet the following criteria:

Minimum dimension for upload: 2048 x 1152 px with an aspect ratio of 16:9.
At the Minimum dimension, the safe area for text and logos: 1235 x 338 px. Larger images may get cropped on certain views or devices.
File size: 6 MB or smaller.
How to resize images

You can use your computer's image editor or an online image resizer to resize the images. For example, you can use Preview on an Quince computer or Microsoft Photos on Windows.

```html
<!DOCTYPE html>
<html lang="en">
<head>
<meta charset="utf-8">
<title>Cozy Nook Attic Sound – Channel Banner</title>
<link rel="stylesheet" href="https://fonts.googleapis.com/css2?family=Marcellus&family=Cormorant+Garamond:ital,wght@1,500&family=Alegreya:wght@700&display=swap">
<style>
  :root {
    --ink-white: #ffffff;
    --ink-soft: #f2f4fa;
    --stage-deep: #04050d;
    --stage-navy: #0a1230;
    --stage-blue: #1f3fa8;
    --stage-glow: #3a63d8;
    --guitar-steel: #2a3447;
    --guitar-dark: #121826;
    --fret-wood: #5a3a30;
    --notes-grey: rgba(200, 205, 215, 0.22);
  }
  html, body {
    margin: 0;
    padding: 0;
    overflow: hidden;
    background: var(--stage-deep);
  }
  .banner {
    position: relative;
    width: 1200px;
    height: 449px;
    overflow: hidden;
    background: var(--stage-deep);
  }
  .banner__backdrop {
    position: absolute;
    inset: 0;
    background:
      radial-gradient(ellipse 300px 240px at 560px 170px, rgba(58, 99, 216, 0.75), rgba(31, 63, 168, 0.25) 60%, transparent 100%),
      radial-gradient(ellipse 260px 300px at 1150px 120px, rgba(31, 63, 168, 0.55), transparent 100%),
      linear-gradient(90deg, var(--stage-navy) 0%, #071030 60%, var(--stage-navy) 100%);
  }
  .banner__guitars {
    position: absolute;
    left: 0;
    top: 0;
    width: 580px;
    height: 449px;
    background:
      linear-gradient(180deg, rgba(90, 58, 48, 0.55) 0%, rgba(90, 58, 48, 0.2) 40%, transparent 55%),
      linear-gradient(100deg, var(--guitar-steel) 0%, #3a4660 30%, var(--guitar-dark) 52%, #26324a 70%, rgba(18, 24, 38, 0.6) 88%, transparent 100%);
    border-radius: 0 0 60% 0 / 0 0 18% 0;
  }
  .banner__notes {
    position: absolute;
    left: 855px;
    top: 122px;
    width: 290px;
    height: 327px;
    background: radial-gradient(ellipse 50% 50% at 50% 55%, var(--notes-grey), transparent 100%);
  }
  .banner__shade {
    position: absolute;
    inset: 0;
    background: linear-gradient(180deg, rgba(0,0,0,0) 55%, rgba(2,3,8,0.8) 100%);
  }
  .banner__text {
    position: absolute;
    left: 538px;
    top: 0;
    color: var(--ink-white);
  }
  .banner__title {
    position: absolute;
    top: 72px;
    left: 0;
    margin: 0;
    white-space: nowrap;
    font-family: "Marcellus", serif;
    font-weight: 400;
    font-size: 51px;
    letter-spacing: -0.5px;
    line-height: 1;
  }
  .banner__byline {
    position: absolute;
    top: 134px;
    left: 2px;
    margin: 0;
    white-space: nowrap;
    font-family: "Cormorant Garamond", serif;
    font-style: italic;
    font-weight: 500;
    font-size: 40px;
    letter-spacing: -1px;
    line-height: 1;
  }
  .banner__line {
    position: absolute;
    left: 2px;
    margin: 0;
    white-space: nowrap;
    font-family: "Alegreya", serif;
    font-weight: 700;
    font-size: 19.5px;
    line-height: 1;
    color: var(--ink-soft);
  }
  .banner__tagline { top: 197px; }
  .banner__topics { top: 231px; }
  .banner__follow { top: 267px; }
  .banner__email {
    top: 307px;
    font-size: 13px;
    letter-spacing: 0.2px;
  }
</style>
</head>
<body>
  <div class="banner">
    <div class="banner__backdrop" role="img" aria-label="Blue-lit stage with soft bokeh lights behind the guitars"></div>
    <div class="banner__guitars" role="img" aria-label="Photo of a row of dark blue electric guitars standing on a rack, necks leaning up to the top edge"></div>
    <div class="banner__notes" role="img" aria-label="Faint grey music notes drifting on a curved staff at the lower right"></div>
    <div class="banner__shade"></div>
    <div class="banner__text">
      <h1 class="banner__title">COZY NOOK ATTIC SOUND</h1>
      <p class="banner__byline">By Dale Harwick</p>
      <p class="banner__line banner__tagline">A Regular Joe Blowin’ his Dough on Gear and Guitars</p>
      <p class="banner__line banner__topics">Music + Gear + Livestreaming + Recording + DAW + Instruments + Vidora</p>
      <p class="banner__line banner__follow">Follow my Studio Renovation | Free How-To’s</p>
      <p class="banner__line banner__email">COZY NOOK ATTIC SOUND@HEARTHMAIL.NET</p>
    </div>
  </div>
</body>
</html>
```